Professional business cards for real estate development company

I need business cards for my new real estate development company. The company, "ORVANE" is a real estate development, investment, and advisory firm with a focus on multifamily, office, and mixed-use projects across primary and secondary markets in the Southeast United States.

Style preference is modern

Industry/Entity Type

Real Estate Development

Contact Information for Business Card

The business cards need to include:
Name
Title
Mailing Address
Phone Number
Web Address

Logo is attached. I would like white to be the primary color with incorporation of the company colors: #232D3A and #B5A451

Font styles to use
Other font styles liked:
• Montserrat, Avenir

Requirements
Must have
• Company Logo. No need to include the company name since the name is in the logo.
Should not have
• No line type designs

```html
<!DOCTYPE html>
<html lang="en">
<head>
<meta charset="UTF-8">
<title>ORVANE Business Cards</title>
<link href="https://fonts.googleapis.com/css2?family=Roboto:wght@400;500;700&display=swap" rel="stylesheet">
<style>
  :root {
    --navy: #232d3a;
    --ink: #1f2a38;
    --paper: #ffffff;
    --backdrop: #e9e9ea;
    --text-soft: #3a4350;
    --rule: #3a4350;
  }
  * { box-sizing: border-box; margin: 0; padding: 0; }
  html, body {
    width: 1200px; height: 801px; overflow: hidden;
    background: var(--backdrop);
    font-family: "Roboto", Arial, sans-serif;
  }
  .stage {
    position: relative; width: 1200px; height: 801px;
    display: flex; align-items: center; justify-content: center; gap: 40px;
  }
  .card {
    position: relative; width: 540px; height: 309px;
    box-shadow: 0 8px 22px rgba(0,0,0,0.18);
  }
  .card--back {
    background: var(--navy);
    display: flex; align-items: center; justify-content: center;
  }
  .card--back .brand-name {
    color: var(--paper); font-weight: 700; font-size: 60px; letter-spacing: 3px;
  }
  .card--front {
    background: var(--paper);
    display: flex; align-items: center;
    padding: 0 30px;
  }
  .front-brand {
    width: 215px; display: flex; align-items: center; gap: 10px;
  }
  .front-brand .brand-square {
    width: 20px; height: 20px; background: var(--ink); flex: none;
  }
  .front-brand .brand-name {
    color: var(--ink); font-weight: 700; font-size: 36px; letter-spacing: 1.5px;
  }
  .divider {
    width: 1.5px; height: 190px; background: var(--rule); margin: 0 22px 0 12px;
  }
  .details { color: var(--ink); }
  .person-name { font-weight: 700; font-size: 21px; letter-spacing: 0.5px; }
  .person-title { font-size: 14px; color: var(--text-soft); margin-top: 2px; }
  .address { font-size: 15px; color: var(--text-soft); margin-top: 12px; line-height: 1.3; }
  .contact-list { list-style: none; margin-top: 10px; }
  .contact-list li {
    display: flex; align-items: center; gap: 10px;
    font-size: 15px; color: var(--text-soft); line-height: 1.55;
  }
  .contact-list svg { width: 13px; height: 13px; flex: none; }
</style>
</head>
<body>
<main class="stage">
  <section class="card card--back" aria-label="Card back">
    <span class="brand-name">ORVANE</span>
  </section>

  <section class="card card--front" aria-label="Card front">
    <div class="front-brand">
      <span class="brand-square"></span>
      <span class="brand-name">ORVANE</span>
    </div>
    <div class="divider"></div>
    <div class="details">
      <p class="person-name">MARCUS HALE</p>
      <p class="person-title">Manager</p>
      <p class="address">Your address, city<br>state, ZIP 0000</p>
      <ul class="contact-list">
        <li>
          <svg viewBox="0 0 24 24" aria-hidden="true"><path fill="#1f2a38" d="M6.6 10.8a15 15 0 0 0 6.6 6.6l2.2-2.2a1 1 0 0 1 1-.25 11.4 11.4 0 0 0 3.6.57 1 1 0 0 1 1 1V20a1 1 0 0 1-1 1A17 17 0 0 1 3 4a1 1 0 0 1 1-1h3.5a1 1 0 0 1 1 1c0 1.25.2 2.45.57 3.57a1 1 0 0 1-.25 1z"/></svg>
          555-014-3872
        </li>
        <li>
          <svg viewBox="0 0 24 24" aria-hidden="true"><rect x="2.5" y="5" width="19" height="14" rx="1.5" fill="none" stroke="#1f2a38" stroke-width="2"/><path d="M3 6l9 7 9-7" fill="none" stroke="#1f2a38" stroke-width="2"/></svg>
          youremail@mailbox.com
        </li>
        <li>
          <svg viewBox="0 0 24 24" aria-hidden="true"><circle cx="12" cy="12" r="9.5" fill="none" stroke="#1f2a38" stroke-width="2"/><path d="M2.5 12h19M12 2.5c3 3 3 16 0 19M12 2.5c-3 3-3 16 0 19" fill="none" stroke="#1f2a38" stroke-width="1.6"/></svg>
          www.yourwebsite.com
        </li>
      </ul>
    </div>
  </section>
</main>
</body>
</html>
```